Brick Paving Company - Pickup Truck and Trailer Wrap Design

**Project Overview:**
We are a brick paving company, specializing in creating beautiful paver patios, walkways, and retaining walls. We're seeking a talented designer on PixelHarbor to create a striking partial or full wrap design for our white pickup truck and trailer. This project demands a balance of creative flair, brand alignment, and a focus on showcasing our services in a visually appealing and professional manner.
**Objectives:**
1. **Brand Consistency:** Employ our provided brand guide and logo to ensure the design aligns with our company's identity.
2. **Flexible Wrap Design:** While our initial preference is for a partial wrap due to budget considerations, we are open to a full wrap design if it significantly enhances the impact and is cost-justifiable.
3. **Service Representation:** Clearly highlight our core services (paver patios, walkways, retaining walls) within the design in an engaging and understandable manner.
4. **Website Synergy:** Take inspiration from the aesthetics of our website for design consistency.
5. **Cost-Effective Solutions:** Prioritize designs that offer the best value for money, balancing visual appeal and budget constraints.

We are excited to see innovative designs that make our company's vehicles stand out, effectively promoting our services.

SEE ATTACHED PHOTOS AND GUIDE

Truck is a 2023 Vortell Haulmax 3500 with Dullies
Trailer is Tundel Haul - you will need to use the attached measuring guide with these measurements provided in inches.

87 3/4 width, 78 1/2 height

A - 191
B - 129 1/2
C - 191
D - 2 7/8
E - 2 3/4
F - 17 1/4 & 7 3/8
G - 38 3/8
H - 75 1/4
I - 85 3/4
J - 68 5/8
K - 12 3/4
L - 5
M - 64 1/2
N - 51
O - 51

Target Market(s)

Please see the Ideal Customer Profile that is attached

Industry/Entity Type

Brick Paving, Hardscape, Outdoor Living

Requirements
Must have
• Include our phone #(877) 555-0183. phone # 877-55-STONE
Nice to have
• Simple and Eye Catching

```html
<!DOCTYPE html>
<html lang="en">
<head>
<meta charset="utf-8">
<title>Corvale Brick Paving – Truck Wrap Layouts</title>
<link href="https://fonts.googleapis.com/css2?family=Montserrat:wght@600;700;800&display=swap" rel="stylesheet">
<style>
  :root {
    --canvas: #ffffff;
    --body-white: #f7f7f7;
    --wrap-black: #0d0d0d;
    --brand-gold: #c9962c;
    --panel-edge: #d9d9d9;
  }
  html, body {
    margin: 0;
    width: 1200px;
    height: 1200px;
    overflow: hidden;
    background: var(--canvas);
  }
  .wrap-sheet {
    position: relative;
    width: 1200px;
    height: 1200px;
  }
  .wrap-layout {
    position: absolute;
    left: 50px;
    width: 1100px;
    height: 240px;
  }
  .wrap-layout--dark-bed { top: 200px; }
  .wrap-layout--light-bed { top: 760px; }
  .brand-name {
    font-family: 'Montserrat', sans-serif;
    font-weight: 800;
    fill: var(--wrap-black);
  }
  .brand-sub {
    font-family: 'Montserrat', sans-serif;
    font-weight: 800;
    fill: var(--wrap-black);
    letter-spacing: 6px;
  }
  .web-address {
    font-family: 'Montserrat', sans-serif;
    font-weight: 800;
    fill: var(--wrap-black);
    letter-spacing: 0.5px;
  }
  .phone {
    font-family: 'Montserrat', sans-serif;
    font-weight: 700;
    letter-spacing: 1px;
  }
  .phone-word { fill: var(--brand-gold); }
  .services {
    font-family: 'Montserrat', sans-serif;
    font-weight: 700;
  }
  .service-arrow { fill: var(--brand-gold); }
  .on-dark { fill: #ffffff; }
  .on-light { fill: var(--wrap-black); }
</style>
</head>
<body>
<main class="wrap-sheet">

  <!-- Layout A: black bed side -->
  <svg class="wrap-layout wrap-layout--dark-bed" viewBox="0 0 1100 240" aria-label="Side wrap layout with black bed panel">
    <rect class="body-panel" x="0" y="0" width="1100" height="240" fill="var(--body-white)" stroke="var(--panel-edge)"/>
    <rect class="bed-panel" x="700" y="0" width="400" height="240" fill="var(--wrap-black)"/>
    <polygon class="sweep-band" points="200,240 200,196 700,110 1100,60 1100,240" fill="var(--wrap-black)"/>
    <polygon class="gold-stripe" points="200,214 1100,114 1100,134 200,234" fill="var(--brand-gold)"/>
    <polygon class="white-pinstripe" points="240,240 1100,146 1100,150 276,240" fill="#ffffff"/>

    <text class="brand-name" x="460" y="95" font-size="48" text-anchor="middle">CORVALE BRICK</text>
    <text class="brand-sub" x="460" y="135" font-size="24" text-anchor="middle">PAVING</text>
    <text class="web-address" x="300" y="217" font-size="12" transform="rotate(-6.34 300 217)">WWW.CORVALEBRICKPAVING.COM</text>

    <text class="phone on-dark" x="740" y="62" font-size="34">877-55-<tspan class="phone-word">STONE</tspan></text>
    <g class="services on-dark" font-size="13">
      <polygon class="service-arrow" points="735,96 740,88 745,96 742,96 742,100 738,100 738,96"/>
      <text x="748" y="100">PAVER PATIOS</text>
      <polygon class="service-arrow" points="858,96 863,88 868,96 865,96 865,100 861,100 861,96"/>
      <text x="871" y="100">WALKWAYS</text>
      <polygon class="service-arrow" points="956,96 961,88 966,96 963,96 963,100 959,100 959,96"/>
      <text x="969" y="100">RETAINING WALLS</text>
    </g>
  </svg>

  <!-- Layout B: white bed side -->
  <svg class="wrap-layout wrap-layout--light-bed" viewBox="0 0 1100 240" aria-label="Side wrap layout with white bed panel">
    <rect class="body-panel" x="0" y="0" width="1100" height="240" fill="var(--body-white)" stroke="var(--panel-edge)"/>
    <polygon class="sweep-band" points="200,240 200,196 700,112 1100,108 1100,240" fill="var(--wrap-black)"/>
    <polygon class="gold-stripe" points="200,214 1100,134 1100,154 200,234" fill="var(--brand-gold)"/>
    <polygon class="white-pinstripe" points="240,240 1100,166 1100,170 276,240" fill="#ffffff"/>

    <text class="brand-name" x="460" y="95" font-size="48" text-anchor="middle">CORVALE BRICK</text>
    <text class="brand-sub" x="460" y="135" font-size="24" text-anchor="middle">PAVING</text>
    <text class="web-address" x="300" y="219" font-size="12" transform="rotate(-5.08 300 219)">WWW.CORVALEBRICKPAVING.COM</text>

    <text class="phone on-light" x="740" y="52" font-size="34">877-55-<tspan class="phone-word">STONE</tspan></text>
    <g class="services on-light" font-size="13">
      <polygon class="service-arrow" points="735,86 740,78 745,86 742,86 742,90 738,90 738,86"/>
      <text x="748" y="90">PAVER PATIOS</text>
      <polygon class="service-arrow" points="858,86 863,78 868,86 865,86 865,90 861,90 861,86"/>
      <text x="871" y="90">WALKWAYS</text>
      <polygon class="service-arrow" points="956,86 961,78 966,86 963,86 963,90 959,90 959,86"/>
      <text x="969" y="90">RETAINING WALLS</text>
    </g>
  </svg>

</main>
</body>
</html>
```